Dune Loop needs some awesome stationary

Do you have what it takes to get my brand? You either do or you don't, have a crack at a design and you my just win my business.

I don't want to waste your or my time, so put your creative genius on either a business card or envelope.

I however need a package of stationary that follows the same brand. I will message you to complete the remaining should I like your first submission.

Here is what I need, have a go!

Basically I need the following for my small business based in melbourne.
- Letterhead (printer ready and MS Word)
- Business Card
- Compliments Slip
- Envelope
- Proposal Cover Page (MS Word only)
- Presentation Folder
- Harbor Tally Cards
- Student Name Tent
- Index Cards
- Tack-Pad

I am establishing the brand and it must be modern, professional but also relaxed; that is not formal and not corporate. It represents a company are leaders, but small enough to care and operate like a bunch of friends. We are bringing people and conversations back to business, and turfing out all the bureaucracy and crazy and wasteful procedures. Its about "lets talk and figure it out together and find even better ways".

Target Market(s)

Mainly companies that build software products, but Agile practices are used in many other industries (even graphic design projects)

Industry/Entity Type

Information Technology

Font styles to use
Sans Serif

Colors
3176b5
aaaaaa

Requirements
Must have
• I like curves and circles and not boxes or rectangles.
• I want a colour rich design with my brand colours, but it must be balanced.
• I want more modern than traditional, but simple modern
Should not have
• Not corporate
• Please don't waste my time if your not going to think about it.
• Don't mess with my primary logo
• Don't change my colours
• Don't overlay logo on image

```html
<!DOCTYPE html>
<html lang="en">
<head>
<meta charset="utf-8">
<title>Dune Loop Letterhead</title>
<link href="https://fonts.googleapis.com/css2?family=Open+Sans:wght@300;400;600;700&display=swap" rel="stylesheet">
<style>
  :root {
    --brand-blue: #3176b5;
    --brand-blue-bright: #1f8fd6;
    --brand-grey: #aaaaaa;
    --paper: #ffffff;
    --backdrop: #b7c1dd;
    --ink-soft: #7d7d86;
  }
  * { box-sizing: border-box; margin: 0; padding: 0; }
  html, body {
    width: 1200px;
    height: 784px;
    overflow: hidden;
    background: var(--backdrop);
    font-family: "Open Sans", sans-serif;
  }
  .letterhead {
    position: absolute;
    left: 338px;
    top: 22px;
    width: 523px;
    height: 740px;
    background: var(--paper);
    box-shadow: 0 6px 18px rgba(40, 50, 90, 0.18);
  }
  .corner-tab {
    position: absolute;
    left: 0;
    top: 0;
    width: 34px;
    height: 7px;
    background: var(--brand-grey);
    opacity: 0.7;
  }
  .brand {
    position: absolute;
    left: 22px;
    top: 22px;
    display: flex;
    align-items: center;
    gap: 8px;
  }
  .brand-dot {
    width: 26px;
    height: 26px;
    border-radius: 50%;
    background: var(--brand-blue);
  }
  .brand-name {
    font-weight: 600;
    font-size: 18px;
    color: var(--brand-blue);
    letter-spacing: 0.2px;
  }
  .header-rule {
    position: absolute;
    left: 88px;
    right: 0;
    top: 82px;
    height: 4px;
    background: linear-gradient(90deg, var(--brand-blue), var(--brand-blue-bright));
  }
  .company {
    position: absolute;
    right: 22px;
    top: 50px;
    text-align: right;
    color: var(--brand-blue);
  }
  .company-name {
    font-weight: 700;
    font-size: 11px;
    line-height: 1.2;
  }
  .company-abn {
    font-weight: 400;
    font-size: 7px;
    line-height: 1.3;
  }
  .contact-row {
    position: absolute;
    left: 22px;
    right: 22px;
    bottom: 20px;
    display: flex;
    justify-content: space-between;
    align-items: center;
    font-weight: 300;
    font-size: 7.5px;
    color: var(--ink-soft);
  }
  .contact-item {
    display: flex;
    align-items: center;
    gap: 5px;
  }
  .contact-icon {
    width: 9px;
    height: 9px;
    fill: var(--brand-blue);
    flex: none;
  }
  .footer-rule {
    position: absolute;
    left: 0;
    right: 0;
    bottom: 0;
    height: 5px;
    background: linear-gradient(90deg, var(--brand-blue-bright), var(--brand-blue));
  }
</style>
</head>
<body>
  <main class="letterhead">
    <div class="corner-tab"></div>

    <header>
      <div class="brand">
        <span class="brand-dot"></span>
        <span class="brand-name">Dune Loop</span>
      </div>
      <div class="company">
        <p class="company-name">Dune Loop Pty Ltd</p>
        <p class="company-abn">ABN No. 42 517 903 286</p>
      </div>
      <div class="header-rule"></div>
    </header>

    <footer>
      <div class="contact-row">
        <span class="contact-item">
          <svg class="contact-icon" viewBox="0 0 10 10" aria-hidden="true"><path d="M5 0.5a3.2 3.2 0 0 1 3.2 3.2C8.2 6 5 9.5 5 9.5S1.8 6 1.8 3.7A3.2 3.2 0 0 1 5 0.5zm0 2a1.2 1.2 0 1 0 0 2.4A1.2 1.2 0 0 0 5 2.5z"/></svg>
          PO Box 4187, Kestrel Heights, VIC 3198, Australia
        </span>
        <span class="contact-item">
          <svg class="contact-icon" viewBox="0 0 10 10" aria-hidden="true"><path d="M2.2 0.6l1.6 2-0.9 1.1c0.6 1.3 1.6 2.3 2.9 2.9l1.1-0.9 2 1.6-0.8 1.8C4.6 9.2 0.8 5.4 0.6 1.4z"/></svg>
          1300DUNELP
        </span>
        <span class="contact-item">
          <svg class="contact-icon" viewBox="0 0 10 10" aria-hidden="true"><path d="M0.5 2h9v6h-9z M0.5 2l4.5 3.5L9.5 2" stroke="#fff" stroke-width="0.8"/></svg>
          hello@dune-loop.com.au
        </span>
        <span class="contact-item">
          <svg class="contact-icon" viewBox="0 0 10 10" aria-hidden="true"><circle cx="5" cy="5" r="4.5"/><path d="M0.5 5h9M5 0.5c2 2.5 2 6.5 0 9M5 0.5c-2 2.5-2 6.5 0 9" stroke="#fff" stroke-width="0.6" fill="none"/></svg>
          www.dune-loop.com.au
        </span>
      </div>
      <div class="footer-rule"></div>
    </footer>
  </main>
</body>
</html>
```